Powerpoint master slide deck for power point presentation by members of my company

To design a master slide deck for powerpoint presentation for a Orthopaedic Clinic Based in Singapore

```html
<!DOCTYPE html>
<html lang="en">
<head>
<meta charset="utf-8">
<title>Stride Joint Clinic – Master Slide Deck</title>
<link href="https://fonts.googleapis.com/css2?family=Ubuntu:wght@300;400;500;700&display=swap" rel="stylesheet">
<style>
:root{
  --teal:#5bb8b2;
  --teal-light:#7fcac5;
  --teal-dark:#2f7c78;
  --teal-deep:#245f5c;
  --grey:#b3b3b3;
  --ink:#3a3a3a;
  --muted:#777;
  --canvas:#d9d9d9;
  --white:#fff;
}
*{box-sizing:border-box;margin:0;padding:0}
html,body{width:1200px;height:2594px;overflow:hidden}
body{background:var(--canvas);font-family:'Ubuntu',sans-serif;color:var(--ink);position:relative}
.abs{position:absolute}

/* decorative area, shown as a soft tonal block */
.ornament{position:absolute;left:63%;top:3%;width:35%;height:94%;border-radius:48% 7% 7% 48% / 30% 7% 7% 30%;background:linear-gradient(165deg,var(--teal) 0%,var(--teal) 45%,#98b8b6 75%,var(--grey) 100%)}
.ornament.light{background:linear-gradient(165deg,#fff 0%,#fff 45%,#e2e2e2 75%,var(--grey) 100%)}
.ornament.low{top:30%;height:67%}

/* hero slide */
.hero{position:absolute;left:145px;top:78px;width:905px;height:508px;background:var(--white);overflow:hidden}
.brand{display:flex;align-items:center;gap:10px;color:#5a5a5a;font-weight:400;white-space:nowrap}
.brand .mark{background:var(--teal);flex:none}
.hero .brand{position:absolute;left:73px;top:78px;font-size:26px;letter-spacing:1px}
.hero .brand .mark{width:38px;height:38px}
.hero-title{position:absolute;left:70px;top:172px;font-size:52px;line-height:56px;color:var(--teal);font-weight:500}
.hero-sub{position:absolute;left:74px;top:294px;font-size:18px;color:var(--ink);font-weight:300}
.date-pill{position:absolute;background:var(--teal-dark);color:#fff;text-align:center}
.hero .date-pill{left:73px;top:388px;width:146px;height:21px;font-size:11px;line-height:21px;font-weight:300}
.copy{position:absolute;left:0;right:0;text-align:center;color:var(--muted);font-weight:300}
.hero .copy{top:481px;font-size:10px}

/* thumbnails */
.thumb{position:absolute;width:372px;height:208px;background:var(--white);overflow:hidden}
.fill{position:absolute;inset:6px;overflow:hidden}
.photo{position:absolute;inset:0}
.thumb .brand{position:absolute;left:30px;top:28px;font-size:10px;gap:5px}
.thumb .brand .mark{width:14px;height:14px}
.t-title{position:absolute;left:30px;top:70px;font-size:20px;line-height:23px;font-weight:400}
.t-sub{position:absolute;left:30px;top:118px;font-size:6.5px;font-weight:300}
.thumb .date-pill{left:30px;top:158px;width:60px;height:7px;font-size:3.5px;line-height:7px}
.thumb .copy{bottom:5px;font-size:3.8px}
.on-dark{color:#fff}
.on-dark .brand{color:#fff}

/* content slides */
.foot-brand{position:absolute;left:8px;bottom:4px;font-size:6px;color:#7a8a8a;display:flex;gap:3px;align-items:center}
.foot-brand i{width:6px;height:6px;background:var(--teal);display:block}
.foot-copy{position:absolute;right:8px;bottom:5px;font-size:3.5px;color:var(--muted)}
.heading{position:absolute;left:0;right:0;top:18px;text-align:center;font-size:13px;font-weight:700;color:var(--ink)}
.heading span{font-weight:400;color:var(--teal)}
.big-label{font-size:13px;font-weight:700;color:var(--ink);line-height:15px}
.big-label span{display:block;font-weight:400;color:var(--teal)}
.txt{font-size:3.6px;line-height:4.6px;color:#666}
.sm-h{font-size:5px;font-weight:500;color:var(--ink)}
.sm-h.teal{color:var(--teal)}
.icon{position:absolute;width:13px;height:13px;border-radius:50%;background:var(--teal)}
.icon.sq{border-radius:2px}
.icon.dark{background:var(--teal-deep)}
.ph{position:absolute}
.contact-h{position:absolute;left:30px;font-size:6px;color:var(--teal);font-weight:500}
.contact-row{position:absolute;left:30px;font-size:3.6px;display:flex;gap:4px;align-items:center}
.contact-row i{width:4px;height:4px;border:0.6px solid currentColor;border-radius:50%;display:block}
table.grid{border-collapse:collapse;font-size:3.6px;color:#555}
table.grid th{background:#555;color:#fff;font-weight:500;height:11px;padding:0 3px;text-align:center}
table.grid th:first-child{text-align:left;background:#444}
table.grid th.hl{background:var(--teal)}
table.grid th.lt{background:#999}
table.grid td{height:10.5px;border-bottom:0.5px solid #ddd;text-align:center;padding:0 3px}
table.grid td:first-child{text-align:left}
</style>
</head>
<body>

<!-- Hero cover slide -->
<section class="hero" aria-label="Cover slide">
  <div class="ornament" role="img" aria-label="Decorative joint swoosh in teal and grey"></div>
  <div class="brand"><span class="mark"></span>STRIDE JOINT CLINIC</div>
  <h1 class="hero-title">Presentation<br>Title Goes Here</h1>
  <p class="hero-sub">Subtitle of Presentation Goes Here</p>
  <div class="date-pill">November 19, 2022</div>
  <p class="copy">© 2022 Copyright STRIDE JOINT CLINIC - All Rights Reserved</p>
</section>

<!-- Row 1: photo covers -->
<div class="thumb" style="left:20px;top:750px">
  <div class="fill on-dark">
    <div class="photo" role="img" aria-label="Dark-toned photo of a clinic patient consultation with faint swoosh lines" style="background:linear-gradient(100deg,#141c1e 30%,#3b4a4c)"></div>
    <div class="brand"><span class="mark"></span>STRIDE JOINT CLINIC</div>
    <div class="t-title" style="color:var(--teal);top:64px">Presentation<br>Title Goes Here</div>
    <div class="t-sub" style="color:var(--teal);top:112px">Subtitle of Presentation Goes Here</div>
    <div class="date-pill" style="top:152px;background:var(--teal)">November 19, 2022</div>
  </div>
  <p class="copy">© 2022 Copyright STRIDE JOINT CLINIC - All Rights Reserved</p>
</div>
<div class="thumb" style="left:411px;top:750px">
  <div class="fill">
    <div class="photo" role="img" aria-label="Teal-tinted photo of a clinic patient consultation with faint swoosh lines" style="background:linear-gradient(100deg,#4fb0aa 30%,#8ccfca)"></div>
    <div class="brand" style="color:#fff"><span class="mark" style="background:#fff"></span>STRIDE JOINT CLINIC</div>
    <div class="t-title" style="color:#2f4f4e;top:64px">Presentation<br>Title Goes Here</div>
    <div class="t-sub" style="color:#2f4f4e;top:112px">Subtitle of Presentation Goes Here</div>
    <div class="date-pill" style="top:152px;background:var(--teal-deep)">November 19, 2022</div>
  </div>
  <p class="copy">© 2022 Copyright STRIDE JOINT CLINIC - All Rights Reserved</p>
</div>
<div class="thumb" style="left:801px;top:750px">
  <div class="fill on-dark">
    <div class="photo" role="img" aria-label="Deep teal-tinted photo of a clinic patient consultation with faint swoosh lines" style="background:linear-gradient(100deg,#245f5c 30%,#4a9692)"></div>
    <div class="brand"><span class="mark" style="background:#fff"></span>STRIDE JOINT CLINIC</div>
    <div class="t-title" style="top:64px">Presentation<br>Title Goes Here</div>
    <div class="t-sub" style="top:112px">Subtitle of Presentation Goes Here</div>
    <div class="date-pill" style="top:152px;background:var(--teal)">November 19, 2022</div>
  </div>
  <p class="copy">© 2022 Copyright STRIDE JOINT CLINIC - All Rights Reserved</p>
</div>

<!-- Row 2 -->
<div class="thumb" style="left:20px;top:978px">
  <div class="fill" style="background:var(--teal)">
    <div class="ornament" role="img" aria-label="Faint decorative swoosh outline on teal" style="background:linear-gradient(165deg,var(--teal),#79c6c1)"></div>
    <div class="brand" style="color:#fff"><span class="mark" style="background:#fff"></span>STRIDE JOINT CLINIC</div>
    <div class="t-title" style="color:#2f4f4e;top:64px">Presentation<br>Title Goes Here</div>
    <div class="t-sub" style="color:#2f4f4e;top:112px">Subtitle of Presentation Goes Here</div>
    <div class="date-pill" style="top:152px;background:var(--teal-deep)">November 19, 2022</div>
  </div>
  <p class="copy">© 2022 Copyright STRIDE JOINT CLINIC - All Rights Reserved</p>
</div>
<div class="thumb" style="left:411px;top:978px">
  <div class="fill">
    <div class="ornament" role="img" aria-label="Decorative joint swoosh in teal and grey"></div>
    <div class="brand"><span class="mark"></span>STRIDE JOINT CLINIC</div>
    <div class="t-title" style="color:var(--teal);top:64px">Presentation<br>Title Goes Here</div>
    <div class="t-sub" style="top:112px">Subtitle of Presentation Goes Here</div>
    <div class="date-pill" style="top:152px">November 19, 2022</div>
  </div>
  <p class="copy">© 2022 Copyright STRIDE JOINT CLINIC - All Rights Reserved</p>
</div>
<div class="thumb" style="left:801px;top:978px;background:var(--teal)">
  <div class="fill" style="background:#fff">
    <div class="ornament" role="img" aria-label="Decorative joint swoosh in teal and white"></div>
    <div class="brand"><span class="mark"></span>STRIDE JOINT CLINIC</div>
    <div class="t-title" style="color:var(--teal);top:64px">Presentation<br>Title Goes Here</div>
    <div class="t-sub" style="top:112px">Subtitle of Presentation Goes Here</div>
    <div class="date-pill" style="top:152px">November 19, 2022</div>
  </div>
  <p class="copy" style="color:#fff">© 2022 Copyright STRIDE JOINT CLINIC - All Rights Reserved</p>
</div>

<!-- Row 3 -->
<div class="thumb" style="left:20px;top:1205px">
  <div class="fill">
    <div class="abs" style="left:0;top:54px;width:64%;height:130px;background:var(--teal)"></div>
    <div class="ornament low" role="img" aria-label="Decorative joint swoosh in teal and grey"></div>
    <div class="brand" style="top:14px"><span class="mark"></span>STRIDE JOINT CLINIC</div>
    <div class="t-title on-dark" style="top:68px">Presentation<br>Title Goes Here</div>
    <div class="t-sub on-dark" style="top:116px">Subtitle of Presentation Goes Here</div>
    <div class="date-pill" style="top:156px">November 19, 2022</div>
  </div>
  <p class="copy">© 2022 Copyright STRIDE JOINT CLINIC - All Rights Reserved</p>
</div>
<div class="thumb" style="left:411px;top:1205px">
  <div class="fill" style="background:var(--teal)">
    <div class="ornament light" role="img" aria-label="Decorative joint swoosh in white and grey"></div>
    <div class="brand" style="color:#fff"><span class="mark" style="background:#fff"></span>STRIDE JOINT CLINIC</div>
    <div class="t-title on-dark">Presentation<br>Title Goes Here</div>
    <div class="t-sub on-dark">Subtitle of Presentation Goes Here</div>
    <div class="date-pill">November 19, 2022</div>
  </div>
  <p class="copy">© 2022 Copyright STRIDE JOINT CLINIC - All Rights Reserved</p>
</div>
<div class="thumb" style="left:801px;top:1205px">
  <div class="fill" style="background:var(--teal)">
    <div class="ornament light" role="img" aria-label="Decorative joint swoosh in white and grey"></div>
    <div class="brand" style="color:#fff"><span class="mark" style="background:#fff"></span>STRIDE JOINT CLINIC</div>
    <div class="t-title on-dark">Presentation<br>Title Goes Here</div>
    <div class="t-sub on-dark">Subtitle of Presentation Goes Here</div>
    <div class="date-pill" style="background:var(--teal-deep)">November 19, 2022</div>
  </div>
  <p class="copy">© 2022 Copyright STRIDE JOINT CLINIC - All Rights Reserved</p>
</div>

<!-- Row 4: content slides -->
<div class="thumb" style="left:20px;top:1433px">
  <div class="abs big-label" style="left:28px;top:72px">ADIPISCING:<span>Elit Vivamus Eu Dui<br>Ex Curabitur</span></div>
  <svg class="abs" style="left:0;top:0" width="372" height="208" viewBox="0 0 372 208"><path d="M112 12 Q200 20 205 104 Q200 188 112 196" fill="none" stroke="#ccc" stroke-width="2"/><circle cx="112" cy="12" r="3" fill="#bbb"/><circle cx="112" cy="196" r="3" fill="#bbb"/></svg>
  <div class="icon" style="left:183px;top:15px"></div>
  <div class="icon dark" style="left:213px;top:49px"></div>
  <div class="icon dark" style="left:221px;top:85px"></div>
  <div class="icon dark" style="left:213px;top:121px"></div>
  <div class="icon" style="left:183px;top:156px"></div>
  <div class="abs" style="left:211px;top:16px"><div class="sm-h teal">Lorem Ipsum Dolor Sit</div><div class="txt">Nullam sit amet magna non ex bibendum<br>mollis. Nunc vel neque eu augue dignissim.</div></div>
  <div class="abs" style="left:241px;top:50px"><div class="sm-h teal">Consectetur Adipiscing Elit</div><div class="txt">Nullam sit amet magna non ex bibendum<br>mollis. Nunc vel neque eu augue dignissim.</div></div>
  <div class="abs" style="left:249px;top:86px"><div class="sm-h">Vivamus Eu Dui Ex</div><div class="txt">Nullam sit amet magna non ex bibendum<br>mollis. Nunc vel neque eu augue dignissim.</div></div>
  <div class="abs" style="left:241px;top:122px"><div class="sm-h teal">Curabitur Dapibus</div><div class="txt">Nullam sit amet magna non ex bibendum<br>mollis. Nunc vel neque eu augue dignissim.</div></div>
  <div class="abs" style="left:211px;top:157px"><div class="sm-h teal">Dignissim Dui, In Molestie</div><div class="txt">Nullam sit amet magna non ex bibendum<br>mollis. Nunc vel neque eu augue dignissim.</div></div>
  <div class="foot-brand"><i></i>STRIDE JOINT CLINIC</div><div class="foot-copy">© 2022 Copyright STRIDE JOINT CLINIC - All Rights Reserved &nbsp;|&nbsp; 10</div>
</div>
<div class="thumb" style="left:411px;top:1433px">
  <div class="heading">Heading <span>Goes Here</span></div>
  <div class="abs" style="left:0;top:50px;width:186px;height:80px;background:var(--teal)"></div>
  <div class="ph" role="img" aria-label="Photo of a doctor writing notes at a desk" style="left:186px;top:50px;width:186px;height:80px;background:linear-gradient(120deg,#e9eef0,#9fb4c4)"></div>
  <div class="icon dark" style="left:16px;top:62px"></div>
  <div class="icon dark" style="left:16px;top:93px"></div>
  <div class="abs on-dark" style="left:48px;top:60px"><div class="sm-h" style="color:#fff">Elit Vivamus Eu Dui Ex Curabitur</div><div class="txt" style="color:#fff">Lorem ipsum dolor sit amet, consectetur adipiscing elit. Vivamus<br>eu dui ex. Curabitur dapibus dignissim dui, in molestie metus<br>feugiat sed. Praesent aliquet lorem ex.</div></div>
  <div class="abs on-dark" style="left:48px;top:92px"><div class="sm-h" style="color:#fff">Donec risus orci, gravida sit</div><div class="txt" style="color:#fff">Lorem ipsum dolor sit amet, consectetur adipiscing elit. Vivamus<br>eu dui ex. Curabitur dapibus dignissim dui, in molestie metus<br>feugiat sed. Praesent aliquet lorem ex.</div></div>
  <div class="abs" style="left:17px;top:136px;width:160px"><div class="sm-h">Elit Vivamus Eu Dui Ex Curabitur</div><div class="txt">Lorem ipsum dolor sit amet, consectetur adipiscing elit. Vivamus eu dui ex. Curabitur dapibus dignissim dui, in molestie metus feugiat sed. Praesent aliquet lorem ex, eu dapibus odio varius at. Duis eget tellus porta, consequat lacus vitae.</div></div>
  <div class="abs" style="left:198px;top:136px;width:160px"><div class="sm-h">Donec risus orci, gravida sit</div><div class="txt">Lorem ipsum dolor sit amet, consectetur adipiscing elit. Vivamus eu dui ex. Curabitur dapibus dignissim dui, in molestie metus feugiat sed. Praesent aliquet lorem ex, eu dapibus odio varius at. Duis eget tellus porta, consequat lacus vitae.</div></div>
  <div class="foot-brand"><i></i>STRIDE JOINT CLINIC</div><div class="foot-copy">© 2022 Copyright STRIDE JOINT CLINIC - All Rights Reserved &nbsp;|&nbsp; 11</div>
</div>
<div class="thumb" style="left:801px;top:1433px">
  <div class="ph" role="img" aria-label="Photo of a nurse with a patient in a wheelchair" style="left:24px;top:0;width:172px;height:117px;background:linear-gradient(140deg,#cfe0ea,#5d8db0)"></div>
  <div class="ph" role="img" aria-label="Photo of a doctor holding a tablet" style="left:24px;top:122px;width:84px;height:56px;background:linear-gradient(140deg,#e8eef0,#a8b9bd)"></div>
  <div class="ph" role="img" aria-label="Photo of a stethoscope on a desk" style="left:112px;top:122px;width:84px;height:56px;background:linear-gradient(140deg,#f2f4f4,#c7cfd0)"></div>
  <div class="abs big-label" style="left:212px;top:20px">Elit Vivamus:<span>Dui Ex Curabitur</span></div>
  <div class="abs txt" style="left:212px;top:56px;width:140px">Lorem ipsum dolor sit amet, consectetur adipiscing elit.<br>Vivamus eu dui ex.</div>
  <div class="abs sm-h teal" style="left:212px;top:78px;font-size:4px">HEADING GOES HERE</div>
  <div class="abs txt" style="left:212px;top:92px;width:140px;line-height:5.2px">• Lorem ipsum dolor sit amet, consectetur adipiscing elit. Vivamus eu dui ex.<br>• Curabitur dapibus dignissim dui, in molestie metus feugiat sed.<br>• Praesent aliquet lorem ex, eu dapibus odio varius at. Duis eget tellus porta, consequat lacus vitae.<br>• Nulla facilisi. In et sollicitudin lacus. Donec risus orci, gravida sit amet risus vehicula, aliquet pretium sapien.</div>
  <div class="foot-brand"><i></i>STRIDE JOINT CLINIC</div><div class="foot-copy">© 2022 Copyright STRIDE JOINT CLINIC - All Rights Reserved &nbsp;|&nbsp; 12</div>
</div>

<!-- Row 5 -->
<div class="thumb" style="left:20px;top:1661px">
  <div class="abs" style="left:0;top:0;width:372px;height:100px;background:var(--teal)"></div>
  <div class="heading" style="color:#fff;font-weight:400;top:10px">Meet Our Team</div>
  <div class="ph" role="img" aria-label="Portrait of team member Ray Tanaka" style="left:18px;top:36px;width:50px;height:54px;background:linear-gradient(#eef3f4,#c9d6d8)"></div>
  <div class="ph" role="img" aria-label="Portrait of team member Mei Lindqvist" style="left:75px;top:36px;width:50px;height:54px;background:linear-gradient(#eef3f4,#c9d6d8)"></div>
  <div class="ph" role="img" aria-label="Portrait of team member Arun Castell" style="left:132px;top:36px;width:50px;height:54px;background:linear-gradient(#eef3f4,#c9d6d8)"></div>
  <div class="ph" role="img" aria-label="Portrait of team member Ray Tanaka" style="left:189px;top:36px;width:50px;height:54px;background:linear-gradient(#eef3f4,#c9d6d8)"></div>
  <div class="ph" role="img" aria-label="Portrait of team member Mei Lindqvist" style="left:246px;top:36px;width:50px;height:54px;background:linear-gradient(#eef3f4,#c9d6d8)"></div>
  <div class="ph" role="img" aria-label="Portrait of team member Arun Castell" style="left:303px;top:36px;width:50px;height:54px;background:linear-gradient(#eef3f4,#c9d6d8)"></div>
  <div class="abs" style="left:18px;top:95px;width:335px;display:grid;grid-template-columns:repeat(6,50px);column-gap:7px;text-align:center">
    <div><div class="sm-h teal" style="font-weight:400;font-size:5.5px">Ray<br>Tanaka</div><div class="txt" style="margin-top:3px">Consectetur Adipiscing Elit. Vivamus Eu Dui Ex.</div><div class="txt" style="margin-top:3px">Lorem ipsum dolor sit amet, consectetur adipiscing elit. Vivamus eu dui ex.</div></div>
    <div><div class="sm-h teal" style="font-weight:400;font-size:5.5px">Mei<br>Lindqvist</div><div class="txt" style="margin-top:3px">Consectetur Adipiscing Elit. Vivamus Eu Dui Ex.</div><div class="txt" style="margin-top:3px">Lorem ipsum dolor sit amet, consectetur adipiscing elit. Vivamus eu dui ex.</div></div>
    <div><div class="sm-h teal" style="font-weight:400;font-size:5.5px">Arun<br>Castell</div><div class="txt" style="margin-top:3px">Consectetur Adipiscing Elit. Vivamus Eu Dui Ex.</div><div class="txt" style="margin-top:3px">Lorem ipsum dolor sit amet, consectetur adipiscing elit. Vivamus eu dui ex.</div></div>
    <div><div class="sm-h teal" style="font-weight:400;font-size:5.5px">Ray<br>Tanaka</div><div class="txt" style="margin-top:3px">Consectetur Adipiscing Elit. Vivamus Eu Dui Ex.</div><div class="txt" style="margin-top:3px">Lorem ipsum dolor sit amet, consectetur adipiscing elit. Vivamus eu dui ex.</div></div>
    <div><div class="sm-h teal" style="font-weight:400;font-size:5.5px">Mei<br>Lindqvist</div><div class="txt" style="margin-top:3px">Consectetur Adipiscing Elit. Vivamus Eu Dui Ex.</div><div class="txt" style="margin-top:3px">Lorem ipsum dolor sit amet, consectetur adipiscing elit. Vivamus eu dui ex.</div></div>
    <div><div class="sm-h teal" style="font-weight:400;font-size:5.5px">Arun<br>Castell</div><div class="txt" style="margin-top:3px">Consectetur Adipiscing Elit. Vivamus Eu Dui Ex.</div><div class="txt" style="margin-top:3px">Lorem ipsum dolor sit amet, consectetur adipiscing elit. Vivamus eu dui ex.</div></div>
  </div>
  <div class="foot-brand"><i></i>STRIDE JOINT CLINIC</div><div class="foot-copy">© 2022 Copyright STRIDE JOINT CLINIC - All Rights Reserved &nbsp;|&nbsp; 13</div>
</div>
<div class="thumb" style="left:411px;top:1661px">
  <div class="abs" style="left:0;top:0;width:135px;height:125px;background:var(--teal);border-radius:0 0 18px 0"></div>
  <div class="abs" style="left:30px;top:30px;font-size:13px;line-height:15px;color:#2f4f4e">Elit Vivamus<br>Eu Dui Ex<br>Curabitur</div>
  <div class="abs txt" style="left:30px;top:86px;width:95px;color:#fff">Lorem ipsum dolor sit amet, consectetur adipiscing elit. Vivamus eu dui ex. Curabitur dapibus dignissim dui, in dapibus odio.</div>
  <div class="icon sq" style="left:150px;top:34px"></div>
  <div class="icon sq dark" style="left:150px;top:82px"></div>
  <div class="icon sq dark" style="left:150px;top:130px"></div>
  <div class="icon sq dark" style="left:258px;top:34px"></div>
  <div class="icon sq" style="left:258px;top:82px"></div>
  <div class="icon sq dark" style="left:258px;top:130px"></div>
  <div class="abs" style="left:176px;top:32px;width:70px"><div class="sm-h teal">Vivamus Eu Dui Ex</div><div class="txt">Praesent aliquet lorem ex, eu dapibus odio varius at. Duis eget tellus porta, consequat lacus vitae.</div></div>
  <div class="abs" style="left:176px;top:80px;width:70px"><div class="sm-h">Gravida Sit Amet Risus</div><div class="txt">Praesent aliquet lorem ex, eu dapibus odio varius at. Duis eget tellus porta, consequat lacus vitae.</div></div>
  <div class="abs" style="left:176px;top:128px;width:70px"><div class="sm-h teal">Nulla Facilisi In Et</div><div class="txt">Praesent aliquet lorem ex, eu dapibus odio varius at. Duis eget tellus porta, consequat lacus vitae.</div></div>
  <div class="abs" style="left:284px;top:32px;width:70px"><div class="sm-h">Nulla Facilisi In Et</div><div class="txt">Praesent aliquet lorem ex, eu dapibus odio varius at. Duis eget tellus porta, consequat lacus vitae.</div></div>
  <div class="abs" style="left:284px;top:80px;width:70px"><div class="sm-h teal">Vivamus Eu Dui Ex</div><div class="txt">Praesent aliquet lorem ex, eu dapibus odio varius at. Duis eget tellus porta, consequat lacus vitae.</div></div>
  <div class="abs" style="left:284px;top:128px;width:70px"><div class="sm-h">Gravida Sit Amet Risus</div><div class="txt">Praesent aliquet lorem ex, eu dapibus odio varius at. Duis eget tellus porta, consequat lacus vitae.</div></div>
  <div class="foot-brand"><i></i>STRIDE JOINT CLINIC</div><div class="foot-copy">© 2022 Copyright STRIDE JOINT CLINIC - All Rights Reserved &nbsp;|&nbsp; 14</div>
</div>
<div class="thumb" style="left:801px;top:1661px">
  <div class="heading">Heading <span>Goes Here</span></div>
  <svg class="abs" style="left:0;top:0" width="372" height="208" viewBox="0 0 372 208"><circle cx="186" cy="112" r="55" fill="none" stroke="#e3e8e8" stroke-width="1"/><rect x="166" y="92" width="40" height="40" fill="var(--teal)"/></svg>
  <div class="icon" style="left:139px;top:66px"></div>
  <div class="icon dark" style="left:220px;top:66px"></div>
  <div class="icon dark" style="left:139px;top:142px"></div>
  <div class="icon" style="left:220px;top:142px"></div>
  <div class="abs" style="left:40px;top:62px;width:90px;text-align:right"><div class="sm-h teal" style="font-weight:400">Nulla Facilisi In Et</div><div class="txt">Curabitur dapibus dignissim dui, in molestie metus feugiat sed. Praesent aliquet lorem ex.</div></div>
  <div class="abs" style="left:246px;top:62px;width:90px"><div class="sm-h" style="font-weight:400">Vivamus Eu Dui Ex</div><div class="txt">Curabitur dapibus dignissim dui, in molestie metus feugiat sed. Praesent aliquet lorem ex.</div></div>
  <div class="abs" style="left:40px;top:138px;width:90px;text-align:right"><div class="sm-h" style="font-weight:400">Elit Vivamus Eu Dui Ex</div><div class="txt">Curabitur dapibus dignissim dui, in molestie metus feugiat sed. Praesent aliquet lorem ex.</div></div>
  <div class="abs" style="left:246px;top:138px;width:90px"><div class="sm-h teal" style="font-weight:400">Gravida Sit Amet Risus</div><div class="txt">Curabitur dapibus dignissim dui, in molestie metus feugiat sed. Praesent aliquet lorem ex.</div></div>
  <div class="foot-brand"><i></i>STRIDE JOINT CLINIC</div><div class="foot-copy">© 2022 Copyright STRIDE JOINT CLINIC - All Rights Reserved &nbsp;|&nbsp; 15</div>
</div>

<!-- Row 6 -->
<div class="thumb" style="left:20px;top:1888px">
  <div class="heading">Heading <span>Goes Here</span></div>
  <div class="abs txt" style="left:0;top:48px;width:372px;height:26px;background:var(--teal);color:#fff;padding:6px 26px;text-align:center">Lorem ipsum dolor sit amet, consectetur adipiscing elit. Vivamus eu dui ex. Curabitur dapibus dignissim dui, in molestie metus feugiat sed. Praesent aliquet lorem ex, eu dapibus odio varius at. Duis eget tellus porta, consequat lacus vitae, venenatis dolor. Nulla facilisi. In et sollicitudin lacus.</div>
  <div class="abs" style="left:63px;top:94px;width:20px;height:20px;background:var(--teal)"></div>
  <div class="abs" style="left:176px;top:94px;width:20px;height:20px;background:var(--teal)"></div>
  <div class="abs" style="left:289px;top:94px;width:20px;height:20px;background:var(--teal)"></div>
  <div class="abs" style="left:26px;top:126px;width:95px;text-align:center"><div class="sm-h" style="font-weight:400">Lorem Ipsum Dolor</div><div class="txt">Lorem ipsum dolor sit amet, consectetur adipiscing elit. Vivamus eu dui ex. Curabitur dapibus dignissim dui, in molestie metus feugiat sed. Praesent aliquet lorem ex.</div></div>
  <div class="abs" style="left:139px;top:126px;width:95px;text-align:center"><div class="sm-h" style="font-weight:400">Consequat Lacus Vitae</div><div class="txt">Lorem ipsum dolor sit amet, consectetur adipiscing elit. Vivamus eu dui ex. Curabitur dapibus dignissim dui, in molestie metus feugiat sed. Praesent aliquet lorem ex.</div></div>
  <div class="abs" style="left:252px;top:126px;width:95px;text-align:center"><div class="sm-h" style="font-weight:400">Bibendum Mollis</div><div class="txt">Lorem ipsum dolor sit amet, consectetur adipiscing elit. Vivamus eu dui ex. Curabitur dapibus dignissim dui, in molestie metus feugiat sed. Praesent aliquet lorem ex.</div></div>
  <div class="foot-brand"><i></i>STRIDE JOINT CLINIC</div><div class="foot-copy">© 2022 Copyright STRIDE JOINT CLINIC - All Rights Reserved &nbsp;|&nbsp; 16</div>
</div>
<div class="thumb" style="left:411px;top:1888px">
  <div class="abs" style="left:240px;top:0;width:132px;height:52px;background:var(--teal)"></div>
  <div class="abs big-label" style="left:30px;top:22px">ADIPISCING:<span>Elit Vivamus Eu Dui<br>Ex Curabitur</span></div>
  <div class="abs txt" style="left:30px;top:76px;width:140px">Lorem ipsum dolor sit amet, consectetur adipiscing elit. Vivamus eu dui ex. Curabitur dapibus dignissim dui, in molestie metus feugiat sed. Praesent aliquet lorem ex, eu dapibus odio varius at. Duis eget tellus porta, consequat lacus vitae, venenatis dolor. Nulla facilisi. In et sollicitudin lacus. Donec risus orci, gravida sit amet risus vehicula, aliquet pretium sapien. Nullam sit amet magna non ex bibendum mollis. Nunc vel neque eu augue dignissim congue ut vitae magna.</div>
  <div class="abs" style="left:190px;top:22px;width:155px;height:38px;background:var(--teal-dark);border-radius:3px;display:flex;align-items:center;gap:8px;padding:0 8px;color:#fff"><span style="font-size:14px">1</span><span class="txt" style="color:#fff;border-left:0.5px solid #fff;padding-left:6px">Lorem ipsum dolor sit amet, consectetur adipiscing elit. Vivamus eu dui ex. Curabitur dapibus dignissim dui.</span></div>
  <div class="abs" style="left:190px;top:68px;width:155px;height:38px;background:#f1f3f3;border-radius:3px;box-shadow:0 1px 2px rgba(0,0,0,.2);display:flex;align-items:center;gap:8px;padding:0 8px;color:var(--teal-dark)"><span style="font-size:14px">2</span><span class="txt" style="border-left:0.5px solid #aaa;padding-left:6px">Lorem ipsum dolor sit amet, consectetur adipiscing elit. Vivamus eu dui ex. Curabitur dapibus dignissim dui.</span></div>
  <div class="abs" style="left:190px;top:114px;width:155px;height:38px;background:#f1f3f3;border-radius:3px;box-shadow:0 1px 2px rgba(0,0,0,.2);display:flex;align-items:center;gap:8px;padding:0 8px;color:var(--teal-dark)"><span style="font-size:14px">3</span><span class="txt" style="border-left:0.5px solid #aaa;padding-left:6px">Lorem ipsum dolor sit amet, consectetur adipiscing elit. Vivamus eu dui ex. Curabitur dapibus dignissim dui.</span></div>
  <div class="foot-brand"><i></i>STRIDE JOINT CLINIC</div><div class="foot-copy">© 2022 Copyright STRIDE JOINT CLINIC - All Rights Reserved &nbsp;|&nbsp; 17</div>
</div>
<div class="thumb" style="left:801px;top:1888px">
  <div class="heading">Heading <span>Goes Here</span></div>
  <svg class="abs" style="left:30px;top:55px" width="185" height="75" viewBox="0 0 185 75" aria-label="Bar chart by category">
    <g font-size="3.5" fill="#777" font-family="Ubuntu,sans-serif"><text x="0" y="5">4</text><text x="0" y="20">3</text><text x="0" y="35">2</text><text x="0" y="50">1</text><text x="0" y="65">0</text></g>
    <line x1="6" y1="64" x2="185" y2="64" stroke="#ccc" stroke-width=".5"/>
    <g fill="var(--teal)"><rect x="14" y="22" width="7" height="42"/><rect x="57" y="30" width="7" height="34"/><rect x="100" y="28" width="7" height="36"/><rect x="143" y="20" width="7" height="44"/></g>
    <g fill="#3e8f8a"><rect x="23" y="36" width="7" height="28"/><rect x="66" y="15" width="7" height="49"/><rect x="109" y="42" width="7" height="22"/><rect x="152" y="32" width="7" height="32"/></g>
    <g fill="var(--teal-deep)"><rect x="32" y="42" width="7" height="22"/><rect x="75" y="38" width="7" height="26"/><rect x="118" y="38" width="7" height="26"/><rect x="161" y="8" width="7" height="56"/></g>
    <g font-size="3.5" fill="#777" font-family="Ubuntu,sans-serif"><text x="18" y="71">Category 1</text><text x="61" y="71">Category 2</text><text x="104" y="71">Category 3</text><text x="147" y="71">Category 4</text></g>
  </svg>
  <div class="abs txt" style="left:30px;top:136px;width:185px">Lorem ipsum dolor sit amet, consectetur adipiscing elit. Vivamus eu dui ex. Curabitur dapibus dignissim dui, in molestie metus feugiat sed. Praesent aliquet lorem ex, eu dapibus odio varius at. Lorem ipsum dolor sit amet, consectetur adipiscing elit. Praesent aliquet lorem ex, eu dapibus odio varius at.</div>
  <div class="abs" style="left:224px;top:52px;width:1px;height:120px;background:#ddd"></div>
  <div class="abs" style="left:234px;top:54px;width:110px"><div class="sm-h teal" style="font-weight:400"><span style="display:inline-block;width:4px;height:4px;background:var(--teal)"></span> Elit Vivamus Eu Dui Ex</div><div class="txt" style="margin-left:7px">Lorem ipsum dolor sit amet, consectetur adipiscing elit. Vivamus eu dui ex. Curabitur dapibus dignissim dui, in molestie metus feugiat sed.</div></div>
  <div class="abs" style="left:234px;top:94px;width:110px"><div class="sm-h" style="font-weight:400;color:#3e8f8a"><span style="display:inline-block;width:4px;height:4px;background:#3e8f8a"></span> Donec risus orci, gravida sit</div><div class="txt" style="margin-left:7px">Lorem ipsum dolor sit amet, consectetur adipiscing elit. Vivamus eu dui ex. Curabitur dapibus dignissim dui, in molestie metus feugiat sed.</div></div>
  <div class="abs" style="left:234px;top:134px;width:110px"><div class="sm-h" style="font-weight:400;color:var(--teal-deep)"><span style="display:inline-block;width:4px;height:4px;background:var(--teal-deep)"></span> Lorem ipsum dolor sit amet</div><div class="txt" style="margin-left:7px">Lorem ipsum dolor sit amet, consectetur adipiscing elit. Vivamus eu dui ex. Curabitur dapibus dignissim dui, in molestie metus feugiat sed.</div></div>
  <div class="foot-brand"><i></i>STRIDE JOINT CLINIC</div><div class="foot-copy">© 2022 Copyright STRIDE JOINT CLINIC - All Rights Reserved &nbsp;|&nbsp; 18</div>
</div>

<!-- Row 7 -->
<div class="thumb" style="left:20px;top:2116px">
  <div class="heading">Heading <span>Goes Here</span></div>
  <table class="grid abs" style="left:18px;top:52px;width:336px">
    <tr><th style="width:104px">Heading Goes Here</th><th class="hl">Heading<br>Goes Here</th><th>Heading<br>Goes Here</th><th style="background:#444">Heading<br>Goes Here</th><th class="lt">Heading<br>Goes Here</th></tr>
    <tr><td>Lorem ipsum dolor sit amet</td><td>23</td><td>12</td><td>78</td><td>78</td></tr>
    <tr><td>Vivamus eu dui ex. Curabitur dapibus</td><td>45</td><td>56</td><td>12</td><td>76</td></tr>
    <tr><td>Praesent aliquet lorem ex, eu dapibus</td><td>78</td><td>76</td><td>34</td><td>34</td></tr>
    <tr><td>Duis eget tellus porta, consequat lacus</td><td>22</td><td>12</td><td>55</td><td>67</td></tr>
    <tr><td>Donec risus orci, gravida sit amet</td><td>34</td><td>66</td><td>45</td><td>11</td></tr>
    <tr><td>Nunc placerat, arcu vel nec mattis</td><td>67</td><td>47</td><td>78</td><td>23</td></tr>
    <tr><td>Nam semper tristique mauris</td><td>87</td><td>67</td><td>12</td><td>45</td></tr>
  </table>
  <div class="abs" style="left:122px;top:50px;width:44px;height:136px;border:1px solid var(--teal);border-radius:3px"></div>
  <div class="foot-brand"><i></i>STRIDE JOINT CLINIC</div><div class="foot-copy">© 2022 Copyright STRIDE JOINT CLINIC - All Rights Reserved &nbsp;|&nbsp; 19</div>
</div>
<div class="thumb" style="left:411px;top:2116px">
  <div class="fill" style="background:var(--teal)">
    <div class="ornament light" role="img" aria-label="Decorative joint swoosh in white and grey"></div>
    <div class="brand" style="color:#fff;top:74px"><span class="mark" style="background:#fff"></span>STRIDE JOINT CLINIC</div>
    <div class="contact-h" style="color:#fff;top:104px">Contact Us</div>
    <div class="abs txt" style="left:30px;top:114px;color:#fff">Lorem ipsum dolor sit amet, consectetur adipiscing<br>elit. Vivamus eu dui ex.</div>
    <div class="contact-row" style="top:130px;color:#fff"><i></i>Lorem ipsum dolor sit amet, consectetur</div>
    <div class="contact-row" style="top:139px;color:#fff"><i></i>Curabitur dapibus dignissim dui</div>
    <div class="contact-row" style="top:148px;color:#fff"><i></i>Donec risus orci, gravida sit amet risus vehicula</div>
  </div>
  <p class="copy">© 2022 Copyright STRIDE JOINT CLINIC - All Rights Reserved</p>
</div>
<div class="thumb" style="left:801px;top:2116px">
  <div class="fill">
    <div class="ornament" role="img" aria-label="Decorative joint swoosh in teal and grey"></div>
    <div class="brand" style="top:74px"><span class="mark"></span>STRIDE JOINT CLINIC</div>
    <div class="contact-h" style="top:104px">Contact Us</div>
    <div class="abs txt" style="left:30px;top:114px">Lorem ipsum dolor sit amet, consectetur adipiscing<br>elit. Vivamus eu dui ex.</div>
    <div class="contact-row" style="top:130px;color:#555"><i style="color:var(--teal)"></i>Lorem ipsum dolor sit amet, consectetur</div>
    <div class="contact-row" style="top:139px;color:#555"><i style="color:var(--teal)"></i>Curabitur dapibus dignissim dui</div>
    <div class="contact-row" style="top:148px;color:#555"><i style="color:var(--teal)"></i>Donec risus orci, gravida sit amet risus vehicula</div>
  </div>
  <p class="copy">© 2022 Copyright STRIDE JOINT CLINIC - All Rights Reserved</p>
</div>

<!-- Row 8 -->
<div class="thumb" style="left:20px;top:2344px;background:var(--teal)">
  <div class="fill" style="background:#fff">
    <div class="ornament" role="img" aria-label="Decorative joint swoosh in teal and white"></div>
    <div class="brand" style="top:74px"><span class="mark"></span>STRIDE JOINT CLINIC</div>
    <div class="contact-h" style="top:104px">Contact Us</div>
    <div class="abs txt" style="left:30px;top:114px">Lorem ipsum dolor sit amet, consectetur adipiscing<br>elit. Vivamus eu dui ex.</div>
    <div class="contact-row" style="top:130px;color:#555"><i style="color:var(--teal)"></i>Lorem ipsum dolor sit amet, consectetur</div>
    <div class="contact-row" style="top:139px;color:#555"><i style="color:var(--teal)"></i>Curabitur dapibus dignissim dui</div>
    <div class="contact-row" style="top:148px;color:#555"><i style="color:var(--teal)"></i>Donec risus orci, gravida sit amet risus vehicula</div>
  </div>
  <p class="copy" style="color:#fff">© 2022 Copyright STRIDE JOINT CLINIC - All Rights Reserved</p>
</div>
<div class="thumb" style="left:411px;top:2344px">
  <div class="fill">
    <div class="photo" role="img" aria-label="Teal-tinted photo of a doctor at a laptop with faint swoosh lines" style="background:linear-gradient(100deg,#4fb0aa 35%,#8ccfca)"></div>
    <div class="brand" style="color:#fff;top:74px"><span class="mark" style="background:#fff"></span>STRIDE JOINT CLINIC</div>
    <div class="contact-h" style="color:#fff;top:104px">Contact Us</div>
    <div class="abs txt" style="left:30px;top:114px;color:#fff">Lorem ipsum dolor sit amet, consectetur adipiscing<br>elit. Vivamus eu dui ex.</div>
    <div class="contact-row" style="top:130px;color:#fff"><i></i>Lorem ipsum dolor sit amet, consectetur</div>
    <div class="contact-row" style="top:139px;color:#fff"><i></i>Curabitur dapibus dignissim dui</div>
    <div class="contact-row" style="top:148px;color:#fff"><i></i>Donec risus orci, gravida sit amet risus vehicula</div>
  </div>
  <p class="copy">© 2022 Copyright STRIDE JOINT CLINIC - All Rights Reserved</p>
</div>
<div class="thumb" style="left:801px;top:2344px">
  <div class="fill">
    <div class="photo" role="img" aria-label="Dark-toned photo of a doctor at a laptop with faint swoosh lines" style="background:linear-gradient(100deg,#141c1e 35%,#3b4a4c)"></div>
    <div class="brand" style="color:#fff;top:74px"><span class="mark"></span>STRIDE JOINT CLINIC</div>
    <div class="contact-h" style="top:104px">Contact Us</div>
    <div class="abs txt" style="left:30px;top:114px;color:#fff">Lorem ipsum dolor sit amet, consectetur adipiscing<br>elit. Vivamus eu dui ex.</div>
    <div class="contact-row" style="top:130px;color:#fff"><i style="color:var(--teal)"></i>Lorem ipsum dolor sit amet, consectetur</div>
    <div class="contact-row" style="top:139px;color:#fff"><i style="color:var(--teal)"></i>Curabitur dapibus dignissim dui</div>
    <div class="contact-row" style="top:148px;color:#fff"><i style="color:var(--teal)"></i>Donec risus orci, gravida sit amet risus vehicula</div>
  </div>
  <p class="copy">© 2022 Copyright STRIDE JOINT CLINIC - All Rights Reserved</p>
</div>

</body>
</html>
```